Business Card Design Project

I am looking for a classy business card design for a product design consultancy. We specialize in Product Design, Prototyping, and Manufacturing Consulting. Products that we design range from consumer electronics to household products all the way to sporting goods. We are based in Arizona and called "Heron Design Works." We like to have fun and goof off as much as we like to create new products. We are young and energetic so we would like our business cards to reflect that. We already have a logo that we would like to implement into the card design. A plain rectangular business card is boring so feel free to get creative, but please, no avocado shaped cards (it's far too literal). Also feel free to play around with textured card stocks or plastic. The final design that we choose will pay attention to all of the little details. Our cards will need to be 2 sided. We're giving you guys free reign to design as you would like. Please have fun with this, it will reflect in our business card.

Thanks guys,
Heron Design Works Team

Industry/Entity Type

Electronics

Requirements
Must have
• We would like to have a spot UV coating somewhere on the business card design if possible.
Nice to have
• Let's see some designs with custom shapes rather than typical rectangular business cards but please no avocado shaped cards, thanks. Also play around with textured card socks.

```html
<!DOCTYPE html>
<html lang="en">
<head>
<meta charset="utf-8">
<title>Heron Design Works – Business Card</title>
<link rel="stylesheet" href="https://fonts.googleapis.com/css2?family=Open+Sans:wght@400;600&display=swap">
<style>
  :root {
    --leaf-green: #8cc63f;
    --deep-green: #2f6b35;
    --moss-green: #4b6a4a;
    --tagline-green: #3d5f2e;
    --silver-light: #e4e6e8;
    --silver-dark: #9a9ea3;
    --blush: #b4717f;
    --paper: #ffffff;
    --ink-light: #ffffff;
  }
  html, body {
    margin: 0;
    padding: 0;
    overflow: hidden;
    background: var(--paper);
  }
  .card-sheet {
    display: block;
    width: 1200px;
    height: 487px;
  }
  .texture-stop-silver-dark { stop-color: var(--silver-dark); }
  .texture-stop-silver-light { stop-color: var(--silver-light); }
  .texture-stop-leaf { stop-color: var(--leaf-green); }
  .texture-stop-moss { stop-color: var(--moss-green); }
  .front-shape {
    stroke: var(--leaf-green);
    stroke-width: 3;
  }
  .back-shape { fill: var(--leaf-green); }
  .contact-panel { fill: var(--blush); }
  .brand-name {
    font-family: "Open Sans", sans-serif;
    font-weight: 400;
  }
  .brand-name--front {
    fill: var(--deep-green);
    font-size: 112px;
    letter-spacing: -2px;
  }
  .brand-name--back {
    fill: var(--ink-light);
    font-size: 104px;
    letter-spacing: -2px;
  }
  .brand-tagline {
    fill: var(--tagline-green);
    font-size: 22px;
  }
  .contact {
    font-family: "Open Sans", sans-serif;
    fill: var(--ink-light);
    font-size: 19px;
  }
  .contact-name { font-weight: 600; }
</style>
</head>
<body>
<svg class="card-sheet" viewBox="0 0 1200 487" xmlns="http://www.w3.org/2000/svg">
  <defs>
    <linearGradient id="front-texture" x1="16" y1="14" x2="600" y2="474" gradientUnits="userSpaceOnUse">
      <stop offset="0" class="texture-stop-silver-dark"/>
      <stop offset="0.3" class="texture-stop-silver-light"/>
      <stop offset="0.5" class="texture-stop-leaf"/>
      <stop offset="0.8" class="texture-stop-moss"/>
      <stop offset="1" class="texture-stop-moss"/>
    </linearGradient>
  </defs>

  <g class="card-front">
    <path class="front-shape" role="img" aria-label="Textured silver and green card stock surface"
          fill="url(#front-texture)"
          d="M40,14 H450 A150,150 0 0 1 600,164 V450 A24,24 0 0 1 576,474 H166 A150,150 0 0 1 16,324 V38 A24,24 0 0 1 40,14 Z"/>
    <text class="brand-name brand-name--front" x="25" y="126">heron</text>
  </g>

  <g class="card-back">
    <path class="back-shape"
          d="M762,14 H1164 A24,24 0 0 1 1188,38 V322 A150,150 0 0 1 1038,472 H636 A24,24 0 0 1 612,448 V164 A150,150 0 0 1 762,14 Z"/>
    <rect class="contact-panel" x="636" y="180" width="344" height="192" rx="28"/>

    <text class="brand-name brand-name--back" x="800" y="110">heron</text>
    <text class="brand-name brand-tagline" x="758" y="141" textLength="415" lengthAdjust="spacing">DESIGN WORKS</text>

    <text class="contact contact-name" x="824" y="214" text-anchor="middle">Dylan Marsh | President</text>
    <text class="contact" x="653" y="262">T.&#160;&#160;480.555.0142 | P.&#160;&#160;602.555.0187</text>
    <text class="contact" x="653" y="316">E.&#160;&#160;dylan@herondesignworks.com</text>
    <text class="contact" x="653" y="343">W.&#160;&#160;www.herondesignworks.com</text>
  </g>
</svg>
</body>
</html>
```